シンプルな名刺が希望です。ロゴの配列及び色は変えてもよいです。
https://www.pelmora.jp/file/message/4733158
表面  会社名 名前 〒 住所 tel  fax アドレス 携帯電話
表面で窮屈であれば裏面も使ってもよいです。
こちらの方が提案者様が使いやすいとの事で、ロゴ作成者様より提案がありました。
https://www.pelmora.jp/file/message/4735157
https://www.pelmora.jp/file/message/4735158
宜しくお願いします。
EPSファイルでロゴを作成したものを添付します。

これなら読めないでしょうか。

シンプルで気に入りました。

ありがとうございました。

```html
<!DOCTYPE html>
<html lang="ja">
<head>
<meta charset="utf-8">
<title>コルヴァン 名刺</title>
<link rel="stylesheet" href="https://fonts.googleapis.com/css2?family=Noto+Serif+JP:wght@400;500&family=Noto+Sans+JP:wght@400;700&family=Josefin+Sans:wght@400&family=Cormorant+Garamond:ital,wght@1,500&display=swap">
<style>
  :root {
    --page: #eef0f3;
    --card: #ffffff;
    --navy: #1f2a5c;
    --ink: #222222;
    --grey: #6e6e70;
    --soft: #e6e7ec;
    --shadow: rgba(20, 25, 45, 0.18);
  }
  html, body {
    margin: 0;
    width: 849px;
    height: 1200px;
    overflow: hidden;
    background: var(--page);
  }
  .card {
    position: absolute;
    left: 161px;
    top: 96px;
    width: 535px;
    height: 1000px;
    background: var(--card);
    box-shadow: 0 4px 14px var(--shadow);
    overflow: hidden;
  }
  .brand-mark {
    position: absolute;
    left: 237px;
    top: 60px;
    width: 62px;
    height: 62px;
    background: var(--navy);
  }
  .brand-name {
    position: absolute;
    left: 0;
    right: 0;
    top: 218px;
    text-align: center;
    font-family: "Josefin Sans", sans-serif;
    font-weight: 400;
    font-size: 52px;
    letter-spacing: 14px;
    padding-left: 14px;
    color: var(--grey);
  }
  .faint-shape {
    position: absolute;
    left: 392px;
    top: 520px;
    width: 200px;
    height: 230px;
    background: var(--soft);
  }
  .person {
    position: absolute;
    left: 107px;
    top: 566px;
  }
  .person-title {
    font-family: "Noto Serif JP", serif;
    font-size: 20px;
    color: var(--ink);
    margin: 0 0 4px;
  }
  .person-name {
    display: flex;
    align-items: baseline;
    gap: 40px;
    margin: 0;
  }
  .name-ja {
    font-family: "Noto Serif JP", serif;
    font-weight: 500;
    font-size: 52px;
    letter-spacing: 6px;
    color: var(--ink);
  }
  .name-en {
    font-family: "Cormorant Garamond", serif;
    font-style: italic;
    font-weight: 500;
    font-size: 26px;
    letter-spacing: 1px;
    color: var(--ink);
  }
  .company {
    position: absolute;
    left: 107px;
    top: 716px;
    margin: 0;
    font-family: "Noto Sans JP", sans-serif;
    font-weight: 700;
    font-size: 25px;
    color: var(--navy);
  }
  .contact {
    position: absolute;
    left: 107px;
    top: 760px;
    margin: 0;
    padding: 0;
    list-style: none;
    font-family: "Noto Sans JP", sans-serif;
    font-size: 20px;
    line-height: 1.18;
    color: var(--navy);
  }
  .contact li {
    display: flex;
    align-items: flex-start;
    margin-bottom: 10px;
  }
  .contact .postal { margin-bottom: 2px; padding-left: 30px; font-size: 18px; }
  .contact .icon {
    width: 22px;
    height: 22px;
    margin-right: 8px;
    flex: none;
    fill: var(--navy);
  }
</style>
</head>
<body>
  <section class="card" aria-label="名刺 表面">
    <div class="brand-mark"></div>
    <div class="brand-name">CORVANE</div>
    <div class="faint-shape"></div>

    <div class="person">
      <p class="person-title">代表取締役</p>
      <p class="person-name">
        <span class="name-ja">三森 亮</span>
        <span class="name-en">Ryo Mimori</span>
      </p>
    </div>

    <h1 class="company">株式会社コルヴァン</h1>

    <ul class="contact">
      <li class="postal">〒150-0041</li>
      <li>
        <svg class="icon" viewBox="0 0 24 24"><path d="M12 3 2 12h3v9h5v-6h4v6h5v-9h3z"/></svg>
        <span>東京都渋谷区神南2-14-8<br>神南ビル4F</span>
      </li>
      <li>
        <svg class="icon" viewBox="0 0 24 24"><path d="M6.6 10.8a15 15 0 0 0 6.6 6.6l2.2-2.2c.3-.3.7-.4 1-.2 1.1.4 2.3.6 3.6.6.6 0 1 .4 1 1V20c0 .6-.4 1-1 1A17 17 0 0 1 3 4c0-.6.4-1 1-1h3.5c.6 0 1 .4 1 1 0 1.3.2 2.5.6 3.6.1.3 0 .7-.2 1z"/></svg>
        <span>03-5550-2841</span>
      </li>
      <li>
        <svg class="icon" viewBox="0 0 24 24"><path d="M7 2h10a1 1 0 0 1 1 1v18a1 1 0 0 1-1 1H7a1 1 0 0 1-1-1V3a1 1 0 0 1 1-1zm1 3v12h8V5zm4 13.5a1 1 0 1 0 0 2 1 1 0 0 0 0-2z"/></svg>
        <span>080-5550-7316</span>
      </li>
      <li>
        <svg class="icon" viewBox="0 0 24 24"><path d="M7 3h8l3 3v4H7zM4 10h16a2 2 0 0 1 2 2v6h-4v3H6v-3H2v-6a2 2 0 0 1 2-2zm4 6v3h8v-3z"/></svg>
        <span>03-5550-2842</span>
      </li>
      <li>
        <svg class="icon" viewBox="0 0 24 24"><path d="M2 5h20v14H2zm2 2v.5l8 5 8-5V7z"/></svg>
        <span>r-mimori@corvane.co.jp</span>
      </li>
    </ul>
  </section>
</body>
</html>
```